Come as U R - mental health service LGBTIQ inclusive poster

We are a mental health organisation in Australia that is looking for a poster design that we can put in our waiting rooms to show that our service is inclusive of gender diverse, intersex, and sexuality diverse people. We will add text and our company logo afterwards. An example has been provided for inspiration. Designers 25 and under encouraged.

Target Market(s)

Target audience - all genders 12-25.

Industry/Entity Type

Mental Health

Requirements
Must have
• This graphic should be colourful, include the text "Come as U R", and incorporate the colours of the pride flag. Should be a general design that is appropriate for all of the target audience.

```html
<!DOCTYPE html>
<html lang="en">
<head>
<meta charset="utf-8">
<title>Come as U R</title>
<link rel="stylesheet" href="https://fonts.googleapis.com/css2?family=Fredoka:wght@600;700&display=swap">
<style>
  :root {
    --red: #e2150f;
    --red-deep: #b50d0a;
    --orange: #e8661b;
    --orange-deep: #c44d10;
    --yellow: #e9c21c;
    --yellow-deep: #c79e0e;
    --green: #2f9b2b;
    --green-deep: #1d7419;
    --blue: #1c52b3;
    --blue-deep: #123a86;
    --purple: #6d2c9c;
    --purple-deep: #4f1b77;
    --ink-blue: #1a47b8;
    --line-yellow: #f6ec12;
    --line-green: #6ee01a;
    --line-purple: #7a1fa6;
    --white: #ffffff;
    --skin-light: #e9c3a6;
    --skin-mid: #c99a7a;
  }
  html, body {
    margin: 0;
    padding: 0;
    width: 849px;
    height: 1200px;
    overflow: hidden;
    background: var(--white);
  }
  .poster {
    display: block;
    width: 849px;
    height: 1200px;
  }
  .headline {
    font-family: "Fredoka", "Arial Rounded MT Bold", sans-serif;
    font-weight: 700;
    stroke-linejoin: round;
  }
  .headline__outline { fill: none; }
  .headline__fill { stroke: none; }

  .headline--come .headline__outline { stroke: var(--ink-blue); stroke-width: 10px; }
  .headline--come .headline__fill { fill: var(--white); }

  .headline--as .headline__outline { stroke: var(--line-yellow); stroke-width: 10px; }
  .headline--as .headline__fill { fill: var(--red); }

  .headline--ur .headline__outline--outer { stroke: var(--white); stroke-width: 20px; }
  .headline--ur .headline__outline--inner { stroke: var(--line-yellow); stroke-width: 9px; }
  .headline--ur .headline__fill { fill: var(--red); }
</style>
</head>
<body>
<svg class="poster" viewBox="0 0 849 1200" xmlns="http://www.w3.org/2000/svg">
  <defs>
    <linearGradient id="tone-red" x1="0" y1="0" x2="1" y2="1"><stop offset="0" stop-color="var(--red)"/><stop offset="1" stop-color="var(--red-deep)"/></linearGradient>
    <linearGradient id="tone-orange" x1="0" y1="0" x2="1" y2="1"><stop offset="0" stop-color="var(--orange)"/><stop offset="1" stop-color="var(--orange-deep)"/></linearGradient>
    <linearGradient id="tone-yellow" x1="0" y1="0" x2="1" y2="1"><stop offset="0" stop-color="var(--yellow)"/><stop offset="1" stop-color="var(--yellow-deep)"/></linearGradient>
    <linearGradient id="tone-green" x1="0" y1="0" x2="1" y2="1"><stop offset="0" stop-color="var(--green)"/><stop offset="1" stop-color="var(--green-deep)"/></linearGradient>
    <linearGradient id="tone-blue" x1="0" y1="0" x2="1" y2="1"><stop offset="0" stop-color="var(--blue)"/><stop offset="1" stop-color="var(--blue-deep)"/></linearGradient>
    <linearGradient id="tone-purple" x1="0" y1="0" x2="1" y2="1"><stop offset="0" stop-color="var(--purple)"/><stop offset="1" stop-color="var(--purple-deep)"/></linearGradient>
    <radialGradient id="tone-portrait" cx="0.5" cy="0.45" r="0.6"><stop offset="0" stop-color="var(--skin-light)"/><stop offset="1" stop-color="var(--skin-mid)"/></radialGradient>
  </defs>

  <g class="portrait-row portrait-row--red" role="img" aria-label="Row of smiling young people tinted red">
    <rect x="0" y="0" width="145" height="205" fill="url(#tone-red)"/>
    <rect x="145" y="0" width="190" height="205" fill="var(--red-deep)"/>
    <rect x="335" y="0" width="205" height="205" fill="url(#tone-red)"/>
    <rect x="540" y="0" width="170" height="205" fill="var(--red-deep)"/>
    <rect x="710" y="0" width="139" height="205" fill="url(#tone-red)"/>
  </g>
  <g class="portrait-row portrait-row--orange" role="img" aria-label="Row of laughing young people tinted orange">
    <rect x="0" y="205" width="150" height="205" fill="url(#tone-orange)"/>
    <rect x="150" y="205" width="190" height="205" fill="var(--orange-deep)"/>
    <rect x="340" y="205" width="200" height="205" fill="url(#tone-orange)"/>
    <rect x="540" y="205" width="180" height="205" fill="var(--orange-deep)"/>
    <rect x="720" y="205" width="129" height="205" fill="url(#tone-orange)"/>
  </g>
  <g class="portrait-row portrait-row--yellow" role="img" aria-label="Row of smiling young people tinted yellow">
    <rect x="0" y="410" width="140" height="190" fill="url(#tone-yellow)"/>
    <rect x="140" y="410" width="200" height="190" fill="var(--yellow-deep)"/>
    <rect x="340" y="410" width="215" height="190" fill="url(#tone-yellow)"/>
    <rect x="555" y="410" width="190" height="190" fill="var(--yellow-deep)"/>
    <rect x="745" y="410" width="104" height="190" fill="url(#tone-yellow)"/>
  </g>
  <g class="portrait-row portrait-row--green" role="img" aria-label="Row of smiling young people tinted green">
    <rect x="0" y="600" width="140" height="195" fill="url(#tone-green)"/>
    <rect x="140" y="600" width="200" height="195" fill="var(--green-deep)"/>
    <rect x="340" y="600" width="200" height="195" fill="url(#tone-green)"/>
    <rect x="540" y="600" width="200" height="195" fill="var(--green-deep)"/>
    <rect x="740" y="600" width="109" height="195" fill="url(#tone-green)"/>
  </g>
  <g class="portrait-row portrait-row--blue" role="img" aria-label="Row of smiling young people tinted blue">
    <rect x="0" y="795" width="160" height="200" fill="url(#tone-blue)"/>
    <rect x="160" y="795" width="200" height="200" fill="var(--blue-deep)"/>
    <rect x="360" y="795" width="190" height="200" fill="url(#tone-blue)"/>
    <rect x="550" y="795" width="190" height="200" fill="var(--blue-deep)"/>
    <rect x="740" y="795" width="109" height="200" fill="url(#tone-blue)"/>
  </g>
  <g class="portrait-row portrait-row--purple" role="img" aria-label="Row of laughing young people tinted purple">
    <rect x="0" y="995" width="150" height="205" fill="url(#tone-purple)"/>
    <rect x="150" y="995" width="190" height="205" fill="var(--purple-deep)"/>
    <rect x="340" y="995" width="200" height="205" fill="url(#tone-purple)"/>
    <rect x="540" y="995" width="190" height="205" fill="var(--purple-deep)"/>
    <rect x="730" y="995" width="119" height="205" fill="url(#tone-purple)"/>
  </g>

  <rect class="feature-portrait" role="img" aria-label="Smiling young woman with long hair" x="380" y="10" width="125" height="170" rx="60" fill="url(#tone-portrait)"/>
  <rect class="feature-portrait" role="img" aria-label="Smiling young woman with brown hair" x="172" y="215" width="130" height="175" rx="55" fill="url(#tone-portrait)"/>
  <rect class="feature-portrait" role="img" aria-label="Smiling young woman with curly blonde hair" x="150" y="600" width="180" height="175" fill="url(#tone-portrait)"/>
  <rect class="feature-portrait" role="img" aria-label="Smiling young man with short hair" x="560" y="800" width="170" height="180" fill="url(#tone-portrait)"/>

  <path class="stripe stripe--white" d="M0 178 L120 172 L300 182 L520 174 L700 180 L849 175 L849 210 L600 205 L380 212 L150 204 L0 208 Z" fill="var(--white)"/>
  <path class="stripe stripe--blue" d="M0 400 L300 406 L560 398 L849 404 L849 420 L500 414 L200 422 L0 416 Z" fill="var(--ink-blue)"/>
  <path class="stripe stripe--purple" d="M0 588 L280 594 L560 586 L849 592 L849 606 L520 600 L240 608 L0 602 Z" fill="var(--line-purple)"/>
  <path class="stripe stripe--yellow" d="M0 784 L260 790 L560 782 L849 788 L849 802 L540 796 L220 804 L0 798 Z" fill="var(--line-yellow)"/>
  <path class="stripe stripe--green" d="M0 984 L300 990 L580 982 L849 988 L849 1002 L560 996 L260 1004 L0 998 Z" fill="var(--line-green)"/>

  <ellipse class="heart-mark" role="img" aria-label="Hand-scribbled green heart" cx="785" cy="70" rx="55" ry="50" fill="var(--line-green)"/>
  <ellipse class="heart-mark" role="img" aria-label="Hand-scribbled yellow heart" cx="620" cy="710" rx="75" ry="60" fill="var(--line-yellow)"/>
  <ellipse class="heart-mark" role="img" aria-label="Hand-scribbled white heart" cx="245" cy="860" rx="68" ry="60" fill="var(--white)"/>
  <ellipse class="heart-mark" role="img" aria-label="Hand-scribbled orange heart" cx="75" cy="1080" rx="60" ry="65" fill="var(--orange)"/>

  <g class="headline headline--come">
    <text class="headline__outline" x="18" y="388" font-size="330" textLength="812" lengthAdjust="spacingAndGlyphs">come</text>
    <text class="headline__fill" x="18" y="388" font-size="330" textLength="812" lengthAdjust="spacingAndGlyphs">come</text>
  </g>

  <g class="headline headline--as">
    <text class="headline__outline" x="268" y="590" font-size="250" textLength="292" lengthAdjust="spacingAndGlyphs">as</text>
    <text class="headline__fill" x="268" y="590" font-size="250" textLength="292" lengthAdjust="spacingAndGlyphs">as</text>
  </g>

  <g class="headline headline--ur">
    <text class="headline__outline headline__outline--outer" x="88" y="1012" font-size="600" textLength="312" lengthAdjust="spacingAndGlyphs">U</text>
    <text class="headline__outline headline__outline--outer" x="455" y="1012" font-size="600" textLength="340" lengthAdjust="spacingAndGlyphs">R</text>
    <text class="headline__outline headline__outline--inner" x="88" y="1012" font-size="600" textLength="312" lengthAdjust="spacingAndGlyphs">U</text>
    <text class="headline__outline headline__outline--inner" x="455" y="1012" font-size="600" textLength="340" lengthAdjust="spacingAndGlyphs">R</text>
    <text class="headline__fill" x="88" y="1012" font-size="600" textLength="312" lengthAdjust="spacingAndGlyphs">U</text>
    <text class="headline__fill" x="455" y="1012" font-size="600" textLength="340" lengthAdjust="spacingAndGlyphs">R</text>
  </g>
</svg>
</body>
</html>
```